Cosmetic Clinic Looking For Sign Designs

We are looking for sign design ideas for the front of our building and a lawn sign for our cosmetic injection salon.
I have uploaded the front of our building for a mock up and size, lawn posts with size and a sign that uses the same dimensions.
We would like both signs to be black for the background.

Target Market(s)

Ages 18-75

Industry/Entity Type

Beauty

Requirements
Must have
• Services we offer:
• Cosmetic Injections
• Airbrush Spray Tanning
• Eyelash Growth Serum
• Skin Care Products & More
• Everything must be on a black background
• The lawn sign must have the address: 394 Fenwick and the building sign should have the phone number.
Should not have
• Nothing can light up (no LED)
• Both signs do not need the full address. Just 394 Fenwick and the phone number

```html
<!DOCTYPE html>
<html lang="en">
<head>
<meta charset="utf-8">
<title>Let's Beam Salon – Lawn Sign</title>
<link href="https://fonts.googleapis.com/css2?family=Poppins:wght@500;600;700&display=swap" rel="stylesheet">
<style>
  :root {
    --page: #e9e9ea;
    --sign-dark: #232325;
    --sign-darker: #1a1a1c;
    --teal: #2fb2c9;
    --pink: #e2207a;
    --white: #ffffff;
    --ink: #1f1f21;
  }
  * { box-sizing: border-box; margin: 0; padding: 0; }
  html, body {
    width: 876px; height: 1200px; overflow: hidden;
    background: var(--page);
    font-family: 'Poppins', Arial, sans-serif;
  }
  .canvas {
    width: 876px; height: 1200px;
    display: flex; align-items: center; justify-content: center;
  }
  .sign {
    width: 816px; height: 720px;
    background: radial-gradient(ellipse at 50% 30%, var(--sign-dark), var(--sign-darker));
    display: flex; flex-direction: column;
    box-shadow: 0 4px 14px rgba(0,0,0,.25);
  }
  .brand {
    display: flex; flex-direction: column; align-items: center;
    padding-top: 34px;
  }
  .brand-dot {
    width: 110px; height: 110px; border-radius: 50%;
    border: 8px solid var(--pink);
    background: #3a3a3d;
  }
  .brand-name {
    margin-top: 18px;
    font-weight: 600; font-size: 58px; line-height: 1;
    letter-spacing: 2px;
    color: var(--teal);
  }
  .services-band {
    margin-top: 40px;
    background: var(--teal);
    text-align: center;
    padding: 14px 0;
  }
  .services-title {
    font-weight: 700; font-size: 60px; line-height: 1.1;
    color: var(--pink); letter-spacing: 1px;
  }
  .services-list {
    flex: 1;
    display: grid; grid-template-columns: 1fr 1fr;
    column-gap: 30px; row-gap: 28px;
    padding: 38px 56px 0 70px;
    list-style: none;
  }
  .service {
    display: flex; align-items: center; gap: 18px;
    color: var(--white);
    font-weight: 600; font-size: 25px; line-height: 1.15;
    text-transform: uppercase;
  }
  .service svg { flex: 0 0 38px; width: 38px; height: 38px; fill: var(--pink); }
  .contact-bar {
    margin: 0 0 22px;
    background: var(--white);
    display: flex; justify-content: space-around; align-items: center;
    height: 78px;
  }
  .contact-item {
    display: flex; align-items: center; gap: 14px;
    font-weight: 700; font-size: 34px;
    text-transform: uppercase;
  }
  .contact-phone { color: var(--pink); }
  .contact-address { color: var(--ink); }
  .contact-item svg { width: 34px; height: 34px; }
</style>
</head>
<body>
<main class="canvas">
  <section class="sign">
    <header class="brand">
      <div class="brand-dot"></div>
      <h1 class="brand-name">LET'S BEAM SALON</h1>
    </header>

    <div class="services-band">
      <h2 class="services-title">SERVICES WE OFFER</h2>
    </div>

    <ul class="services-list">
      <li class="service">
        <svg viewBox="0 0 24 24" aria-hidden="true"><rect x="3" y="10" width="14" height="5" rx="1" transform="rotate(-45 10 12.5)"/><rect x="16" y="3" width="2" height="6" transform="rotate(45 17 6)"/></svg>
        Cosmetic Injections
      </li>
      <li class="service">
        <svg viewBox="0 0 24 24" aria-hidden="true"><rect x="6" y="9" width="10" height="13" rx="2"/><rect x="8" y="4" width="6" height="5"/><rect x="14" y="4" width="5" height="2"/></svg>
        Airbrush Spray Tanning
      </li>
      <li class="service">
        <svg viewBox="0 0 24 24" aria-hidden="true"><path d="M2 12c3-5 7-7 10-7s7 2 10 7c-3 5-7 7-10 7s-7-2-10-7z"/><circle cx="12" cy="12" r="3" fill="#232325"/></svg>
        Eyelash Growth Serum
      </li>
      <li class="service">
        <svg viewBox="0 0 24 24" aria-hidden="true"><rect x="4" y="8" width="8" height="14" rx="2"/><rect x="6" y="4" width="4" height="4"/><rect x="14" y="13" width="7" height="9" rx="1.5"/></svg>
        Skin Care Products &amp; More
      </li>
    </ul>

    <footer class="contact-bar">
      <div class="contact-item contact-phone">
        <svg viewBox="0 0 24 24" aria-hidden="true"><path fill="#e2207a" d="M6.6 10.8c1.4 2.8 3.8 5.2 6.6 6.6l2.2-2.2c.3-.3.7-.4 1-.2 1.1.4 2.3.6 3.6.6.6 0 1 .4 1 1V20c0 .6-.4 1-1 1C10.6 21 3 13.4 3 4c0-.6.4-1 1-1h3.5c.6 0 1 .4 1 1 0 1.3.2 2.5.6 3.6.1.3 0 .7-.2 1l-2.3 2.2z"/></svg>
        (555) 014-2210
      </div>
      <div class="contact-item contact-address">
        <svg viewBox="0 0 24 24" aria-hidden="true"><path fill="#1f1f21" d="M12 2a7 7 0 0 0-7 7c0 5.2 7 13 7 13s7-7.8 7-13a7 7 0 0 0-7-7zm0 9.5A2.5 2.5 0 1 1 12 6.5a2.5 2.5 0 0 1 0 5z"/></svg>
        394 Fenwick
      </div>
    </footer>
  </section>
</main>
</body>
</html>
```